Poster Design Project

We are youth orchestra in Texas that is introducing a new summer program called: Riverbend Bow Academy (It's for students ages 8-18 who play already play violin/viola/cello/bass

Poster size: 11" by 17"

All the details are below, but on the poster we would need the website listed: www.marlowvalleyensemble.example and tell them to go to that website to apply online beginning April 1st

That's how we get business, they go to our website and apply. It also needs to say really big MVE RIVERBEND BOW ACADEMY

We want to use these posters every summer so no dates on it please. Only: April 1st is when we being accepting online applications (every year, so don't put a year) Also put: Camp is held on Saturdays in June and July with final concert, last Sunday in July

Also on the poster we need: Our goal is to keep young musicians playing over the summer –so don’t put your instrument away for the summer! Keep in shape by joining us for the Marlow Valley Ensemble’s summer program – Riverbend Bow Academy! Tuition is $225, which covers June/July Saturday rehearsals and the performance fee for the HPSD Hall concert, last Sunday in July.

I know we can't get all the info below on it, but I put it on so you could better understand what we are doing.

We have a logo already, that we have the rights to - I need something that kids/teens will think is cool looking and music related....we are string instruments only (violin, viola, cello, bass) we also want it to look classy looking, not cheap
I included 2 copies of the logo in different color set

here's all the details from our website:
Riverbend Bow Academy (June and July) - Tuition: $225

Rehearsals on Saturdays June &July with final concert on last Sunday in July @ HPHS Hall

Our goal is to keep young musicians playing over the summer –so don’t put your instrument away for the summer! Keep in shape by joining us for the Marlow Valley Ensemble’s new summer program – Riverbend Bow Academy!

Tuition is $225, which covers June/July Saturday rehearsals and the performance fee for the HPSD Hall concert.

No audition is necessary. Enrollment is limited to the first 50 students in each age category, depending on instrumentation needs, so don’t delay – enrollment online begins April 1st. Siblings will receive a $50 discount, after the first child's regular priced tuition.

Riverbend Bow I: Students entering grades 6 and below (3:00 – 4:20 P.M. )
Riverbend Bow II: Students grades entering 7 and 8 (4:30 – 6:00 P.M.)
Riverbend Bow III: Students entering grades 9-12 (6:15 – 7:45 P.M.)

Summer camp attendance policy is more lenient due to summer vacations. Please notify MVE of summer absences as soon as your vacation/camp dates are known.

Target Market(s)

string players ages 10-18 and their parents

Industry/Entity Type

Business

Requirements
Must have
• Be able to see title from far, and prominently display how/when to apply and where (website)

Also only the concert is at HPHS Hall, we rehearse at Fenwick Music in Allen

I'm working on uploading files for our QR codes for website and phone - It's uploaded below
Nice to have
• If you have room, the Riverbend Bow Academy I II and III times/grades, etc. but doesn't have to be seen as prominently as the title and how to apply
Should not have
• pictures of violin/vla/cello/bass students if they look elementary aged, should be more in the teenager age group if you use pictures.

```html
<!DOCTYPE html>
<html lang="en">
<head>
<meta charset="utf-8">
<title>MVE Riverbend Bow Academy</title>
<link href="https://fonts.googleapis.com/css2?family=Archivo+Black&family=Arimo:wght@400;700&display=swap" rel="stylesheet">
<style>
  :root {
    --paper: #ffffff;
    --ink: #000000;
    --yellow: #ffec00;
    --green: #39d12a;
    --band-green: #2fbf2a;
    --white: #ffffff;
    --rule: #5a5a5a;
    --photo-dark: #1a1a1a;
    --photo-grey: #6d6d6d;
    --photo-light: #b9b9b9;
    --photo-wood: #5a1e12;
  }
  html, body {
    margin: 0;
    padding: 0;
    width: 776px;
    height: 1200px;
    overflow: hidden;
    background: var(--paper);
  }
  .poster {
    position: absolute;
    left: 35px;
    top: 35px;
    width: 706px;
    height: 1135px;
    background: var(--ink);
    overflow: hidden;
    font-family: "Arimo", Arial, sans-serif;
    color: var(--white);
  }
  .title {
    position: absolute;
    left: 24px;
    top: 14px;
    margin: 0;
    color: var(--yellow);
    font-weight: 400;
  }
  .title .org {
    display: block;
    font-family: "Arimo", Arial, sans-serif;
    font-weight: 700;
    font-size: 84px;
    line-height: 92px;
    letter-spacing: 1px;
  }
  .title .program {
    display: block;
    font-size: 60px;
    line-height: 68px;
    letter-spacing: 0.5px;
  }
  .audience-band {
    position: absolute;
    left: 0;
    top: 252px;
    width: 420px;
    height: 84px;
    background: linear-gradient(90deg, var(--band-green) 0%, var(--band-green) 45%, rgba(47,191,42,0) 100%);
  }
  .audience {
    position: absolute;
    left: 12px;
    top: 257px;
    margin: 0;
    font-weight: 700;
    font-size: 17.5px;
    line-height: 24px;
    color: var(--white);
  }
  .brand {
    position: absolute;
    left: 60px;
    top: 348px;
    width: 600px;
    height: 100px;
    display: flex;
    align-items: center;
    gap: 18px;
    color: var(--white);
    font-weight: 700;
  }
  .brand-dot {
    width: 54px;
    height: 54px;
    border-radius: 50%;
    background: var(--white);
    flex: none;
  }
  .brand-name {
    font-size: 22px;
    letter-spacing: 2px;
    text-transform: uppercase;
  }
  .brand-mark {
    font-size: 96px;
    line-height: 1;
    margin-left: auto;
  }
  .horizon {
    position: absolute;
    left: 0;
    top: 456px;
    width: 706px;
    height: 2px;
    background: linear-gradient(90deg, rgba(90,90,90,0), var(--rule) 20%, var(--rule) 80%, rgba(90,90,90,0));
  }
  .details {
    position: absolute;
    left: 72px;
    top: 474px;
    margin: 0;
    font-weight: 700;
    font-size: 19px;
    line-height: 27px;
  }
  .details p { margin: 0; }
  .details .label { color: var(--yellow); font-size: 20px; }
  .details .gap { margin-top: 4px; }
  .photo {
    position: absolute;
    left: 0;
    top: 660px;
    width: 706px;
    height: 475px;
    background:
      radial-gradient(ellipse 300px 120px at 170px 430px, var(--photo-wood) 0%, rgba(90,30,18,0.8) 50%, rgba(90,30,18,0) 100%),
      linear-gradient(175deg, var(--ink) 0%, var(--photo-dark) 25%, var(--photo-grey) 45%, var(--photo-light) 55%, var(--photo-grey) 68%, var(--photo-dark) 85%, var(--ink) 100%);
  }
  .sessions {
    position: absolute;
    left: 0;
    top: 696px;
    width: 706px;
    display: flex;
    justify-content: space-between;
  }
  .session {
    width: 233px;
    text-align: center;
    font-weight: 700;
    font-size: 14.5px;
    line-height: 19px;
  }
  .session h2 {
    margin: 0 0 4px;
    color: var(--green);
    font-size: 18px;
    line-height: 25px;
  }
  .session .note { font-size: 13px; line-height: 18px; }
  .divider {
    width: 2px;
    height: 140px;
    background: var(--white);
    flex: none;
    margin-top: 2px;
  }
  .apply {
    position: absolute;
    left: 0;
    top: 963px;
    width: 706px;
    margin: 0;
    text-align: center;
    color: var(--yellow);
    font-family: "Archivo Black", "Arimo", sans-serif;
    font-weight: 400;
    font-size: 33px;
    line-height: 43px;
    letter-spacing: 1px;
    text-shadow: 2px 3px 4px rgba(0,0,0,0.85);
  }
  .apply .url {
    display: block;
    font-family: "Arimo", Arial, sans-serif;
    font-weight: 700;
    font-size: 25px;
    line-height: 40px;
    letter-spacing: 0.5px;
  }
  .credit {
    position: absolute;
    right: 8px;
    bottom: 6px;
    margin: 0;
    font-size: 9px;
    color: var(--white);
  }
</style>
</head>
<body>
  <main class="poster">
    <h1 class="title">
      <span class="org">MVE</span>
      <span class="program">RIVERBEND BOW</span>
      <span class="program">ACADEMY</span>
    </h1>

    <div class="audience-band"></div>
    <p class="audience">For students ages 8-18 years old<br>who already play the violin, viola,<br>cello and bass.</p>

    <div class="brand">
      <span class="brand-dot"></span>
      <span class="brand-name">Marlow Valley Ensemble</span>
      <span class="brand-mark">MVE</span>
    </div>
    <div class="horizon"></div>

    <section class="details">
      <p class="label">OUR GOAL:</p>
      <p>To keep young musicians playing over the summer.</p>
      <p class="gap"><span class="label">TUITION:</span>&nbsp; $225</p>
      <p class="gap"><span class="label">CAMP:</span> Rehearsals every Saturday in June &amp; July</p>
      <p>with final concert at HPHS Hall, last Sunday in July.</p>
    </section>

    <div class="photo" role="img" aria-label="Photograph of sheet music with a violin in the lower left corner"></div>

    <section class="sessions">
      <div class="session">
        <h2>RIVERBEND<br>BOW I:</h2>
        Students in<br>grades 6 &amp; below<br>
        <span class="note">(grade for next school<br>year with at least 1 year<br>playing experience)</span><br>
        3:00 – 4:20 P.M.
      </div>
      <div class="divider"></div>
      <div class="session">
        <h2>RIVERBEND<br>BOW II:</h2>
        Students in<br>grades 7 &amp; 8<br>
        <span class="note">(grade for next school yr.)</span><br>
        4:30 – 6:00 P.M.
      </div>
      <div class="divider"></div>
      <div class="session">
        <h2>RIVERBEND<br>BOW III:</h2>
        Students in<br>grades 9-12<br>
        <span class="note">(grade for next school yr.)</span><br>
        6:15 – 7:45 P.M.
      </div>
    </section>

    <p class="apply">
      Applications Taken Online<br>
      Beginning April 1st
      <span class="url">www.marlowvalleyensemble.example</span>
    </p>

    <p class="credit">Image courtesy of Lumenstock.example</p>
  </main>
</body>
</html>
```